Design a Professional Business Card for Velmora Arcs

Design a business card for Velmora Arcs, we are a National Sport Court Company.

West Region Address: 4175 Quill Harbor Ln, Suite #215 Englewood, Colorado 80467
East Region Address: 3817 Tamsin Rd E, Bradenton, Florida 34583

Target Market(s)

High End Residential & Institutional Clients

Industry/Entity Type

Design & Construction

Contact Information for Business Card

Logo/Brand/Colors/ name, number (provided in comments)

Requirements
Must have
• Colors only provided in logo
Should not have
• Any other colors not in existing logo (attached)

```html
<!DOCTYPE html>
<html lang="en">
<head>
<meta charset="utf-8">
<title>Velmora Arcs — Business Card</title>
<link rel="stylesheet" href="https://fonts.googleapis.com/css2?family=Montserrat:wght@500;600;700&display=swap">
<style>
  :root {
    --navy: #1f3a70;
    --green: #1d7a3c;
    --ink: #141414;
    --paper: #ffffff;
    --backdrop: #2b2d31;
  }
  * { box-sizing: border-box; margin: 0; padding: 0; }
  html, body { width: 1200px; height: 1200px; overflow: hidden; }
  body {
    background: var(--backdrop);
    font-family: "Montserrat", Arial, sans-serif;
    color: var(--ink);
    position: relative;
  }
  .card {
    position: absolute;
    left: 180px;
    width: 840px;
    height: 480px;
    border-radius: 40px;
    overflow: hidden;
  }
  .card-front { top: 70px; background: var(--paper); }
  .card-back  { top: 650px; background: var(--navy); }

  .brand { display: flex; align-items: center; gap: 22px; }
  .brand-mark { width: 86px; height: 86px; border-radius: 50%; background: var(--navy); flex: none; }
  .brand-name {
    font-weight: 700; font-size: 46px; line-height: 1;
    letter-spacing: 3px; text-transform: uppercase; color: var(--navy);
  }
  .card-front .brand { position: absolute; left: 56px; top: 44px; }

  .divider {
    position: absolute; left: 56px; right: 56px; top: 168px;
    height: 3px; background: var(--green);
  }
  .person { position: absolute; right: 56px; top: 190px; text-align: right; }
  .person-name { font-weight: 700; font-size: 30px; letter-spacing: 0.5px; text-transform: uppercase; }
  .person-title { font-weight: 500; font-size: 24px; margin-top: 6px; }

  .contacts {
    position: absolute; left: 56px; bottom: 48px;
    list-style: none; font-size: 17px; font-weight: 500; line-height: 1.75;
  }
  .contacts li { display: flex; align-items: center; gap: 12px; }
  .contacts svg { width: 16px; height: 16px; fill: var(--green); flex: none; }

  .offices {
    position: absolute; right: 56px; bottom: 48px;
    text-align: right; font-size: 18px; font-weight: 500; line-height: 1.45;
  }
  .region { color: var(--green); font-weight: 600; }

  .card-back .brand {
    position: absolute; left: 50%; top: 50%; transform: translate(-50%, -50%);
    gap: 16px;
  }
  .card-back .brand-mark { width: 56px; height: 56px; background: var(--green); }
  .card-back .brand-name { color: var(--paper); font-size: 34px; }
</style>
</head>
<body>
  <section class="card card-front">
    <div class="brand">
      <span class="brand-mark"></span>
      <span class="brand-name">Velmora Arcs</span>
    </div>
    <div class="divider"></div>
    <div class="person">
      <p class="person-name">Dorian R. Halloway, ASLA</p>
      <p class="person-title">CEO &amp; Founder</p>
    </div>
    <ul class="contacts">
      <li><svg viewBox="0 0 16 16"><path d="M3 1l3 3-2 2c1 2 3 4 5 5l2-2 3 3-2 3C7 15 1 9 0 4z"/></svg>Direct: (303) 555-0147</li>
      <li><svg viewBox="0 0 16 16"><path d="M3 1l3 3-2 2c1 2 3 4 5 5l2-2 3 3-2 3C7 15 1 9 0 4z"/></svg>Main: 1-800-555-0193</li>
      <li><svg viewBox="0 0 16 16"><path d="M0 3h16v10H0z M1 4l7 5 7-5" fill="none" stroke="#1d7a3c" stroke-width="1.6"/></svg>dorian@velmoraarcs.com</li>
      <li><svg viewBox="0 0 16 16"><circle cx="8" cy="8" r="7" fill="none" stroke="#1d7a3c" stroke-width="1.6"/><path d="M1 8h14M8 1c-3 4-3 10 0 14M8 1c3 4 3 10 0 14" fill="none" stroke="#1d7a3c" stroke-width="1.2"/></svg>www.velmoraarcs.com</li>
    </ul>
    <div class="offices">
      <p class="region">West Region</p>
      <p>4175 Quill Harbor Ln, Suite #215</p>
      <p>Englewood, Colorado 80467</p>
      <p class="region">East Region</p>
      <p>3817 Tamsin Rd E, Bradenton</p>
      <p>Florida 34583</p>
    </div>
  </section>

  <section class="card card-back">
    <div class="brand">
      <span class="brand-mark"></span>
      <span class="brand-name">Velmora Arcs</span>
    </div>
  </section>
</body>
</html>
```